Letterhead

We are looking for a basic letterhead. It should include our logo, website - northpeakkitchenware.com, phone 907.418.3952, toll free 855.392.6180, and fax 907.418.5263, along with our address 4837 Birchwood Lane, Anchorage, AK 99517. I want something that will look good printed in color or black and white.

```html
<!DOCTYPE html>
<html lang="en">
<head>
<meta charset="utf-8">
<title>North Peak Kitchenware — Letterhead</title>
<link rel="stylesheet" href="https://fonts.googleapis.com/css2?family=Roboto:wght@400;700;900&display=swap">
<style>
  :root {
    --backdrop: #ffffff;
    --paper: #ffffff;
    --shade-dark: #3b3b3b;
    --shade-mid: #9a9a9a;
    --brand-blue: #1f4d9c;
    --text-gray: #555555;
    --rule-gray: #8a8a8a;
    --footer-rule: #d6d6d6;
  }
  * { box-sizing: border-box; margin: 0; padding: 0; }
  html, body {
    width: 1200px;
    height: 972px;
    overflow: hidden;
    background: var(--backdrop);
    font-family: "Roboto", Arial, sans-serif;
  }
  .letterhead {
    position: absolute;
    left: 252px;
    top: 36px;
    width: 696px;
    height: 900px;
    background:
      linear-gradient(to bottom,
        var(--shade-dark) 0%,
        var(--shade-mid) 6%,
        #e6e6e6 16%,
        var(--paper) 28%,
        var(--paper) 66%,
        #e4e4e4 80%,
        var(--shade-mid) 92%,
        var(--shade-dark) 100%);
    box-shadow: 0 0 0 1px #e2e2e2;
  }
  .brand {
    position: absolute;
    left: 52px;
    top: 92px;
    color: var(--brand-blue);
    font-weight: 900;
    line-height: 1;
  }
  .brand-name {
    font-size: 44px;
    letter-spacing: 0.5px;
    text-transform: uppercase;
    display: block;
  }
  .brand-line {
    font-size: 19px;
    letter-spacing: 2.6px;
    text-transform: uppercase;
    display: block;
    margin-top: 6px;
  }
  .contact {
    position: absolute;
    left: 412px;
    top: 84px;
    padding-left: 14px;
    border-left: 2px solid var(--rule-gray);
    color: var(--text-gray);
    font-size: 11.5px;
    line-height: 19px;
    list-style: none;
  }
  .contact .label { font-weight: 700; margin-right: 4px; }
  .footer-rule {
    position: absolute;
    left: 52px;
    right: 52px;
    bottom: 70px;
    height: 2px;
    background: var(--footer-rule);
  }
</style>
</head>
<body>
  <main class="letterhead">
    <div class="brand">
      <span class="brand-name">North Peak</span>
      <span class="brand-line">Kitchenware</span>
    </div>
    <ul class="contact">
      <li><span class="label">A:</span>4837 Birchwood Lane Anchorage AK 99517</li>
      <li><span class="label">T:</span>907.418.3952, 855.392.6180</li>
      <li><span class="label">F:</span>907.418.5263</li>
      <li><span class="label">W:</span>www.northpeakkitchenware.com</li>
    </ul>
    <div class="footer-rule"></div>
  </main>
</body>
</html>
```